San Francisco Leading Consulting firm - 47Nova Web Design Project

•Create a Web Design
•Uncoded webpage layout design
•2 Pages Design - Homepage + Interior Page

Task Description
Hello, we're looking for a re-design our current website www.47nova-example.com

we have a sample mockup design @

http://47nova.civicpane-example.org/

This shows the layout that we like and also a sample of 6 pictures that would change based on where you mouse over..

6 pictures HOME design needs to be included.

SMART
THOUGHTFUL
FLEXIBLE
CREATIVE SERVICES
TECHNICAL SERVICES
PARTNERS

sites we like:

http://www.brelmoradvisory-example.com/Home.cfm?id=Home
http://www.pixelquarry-example.com/index.html

Our company can be best described as: 100+ employees, cutting-edge, depandable, innovative, strong, smart.

Our Primary focus is: IT Consulting Services and Creative Design services

47Nova LLC is a consulting firm providing creative design, business and technology solutions to both private and public interests.

Established in 1996, 47Nova is a San Francisco based company providing specialists for a range of business needs including:

Creative Design Services
•Print
•Logo Design
•Website Design
•Illustration

and

Business and Technology solutions

•Application Software and Web Development
•Business Process Re-Design (BPR)
•Business/Systems Analysis and Requirement Documentation
•Mentoring and Training
•Network/Hardware Installation Services
•System Design and Architecture
•Vendor Management
•Teamvault Architecture and Implementation

our sample mockup site:

Reason: Due to holiday season, we're not available to work with designers and finilize our design.  

Thank you very much for submitting your design.

We appreciate your time and creativity.   Since, our office is currently closed for holidays, we will be reviewing it in details next week and will make our decision as soon as possible.

It would be great if you could submit any of your changes by Wed next week, so it would be part of our reviews. 

Please see updated wireframe under attachments:  we have some minor updates to our wireframe that we would like you to update your designs, if possible.  

We also encorouge you not to use our standard wireframe and come up with more unique designs.   Everything would be considered when we review your design.

 

Target Market(s)

Creative services and professional services clients, including government agencies

Industry/Entity Type

Business

Requirements
Must have
• Clean, professional look, easy navigation

```html
<!DOCTYPE html>
<html lang="en">
<head>
<meta charset="utf-8">
<title>47Nova — Home</title>
<link href="https://fonts.googleapis.com/css2?family=Arimo:wght@400;700&display=swap" rel="stylesheet">
<style>
  :root{
    --backdrop:#a3a3a3;
    --page:#ffffff;
    --nav:#8b8b8b;
    --nav-line:#b9b9b9;
    --accent:#d0121b;
    --ink:#333333;
    --heading:#5a5a5a;
    --muted:#7a7a7a;
    --rule:#d6d6d6;
    --caption-band:rgba(40,44,40,.62);
  }
  *{box-sizing:border-box;margin:0;padding:0}
  html,body{width:1200px;height:900px;overflow:hidden}
  body{background:var(--backdrop);font-family:"Arimo",Arial,sans-serif;color:var(--ink);position:relative}
  .page{position:absolute;left:44px;top:44px;width:1112px;height:776px;background:var(--page)}
  .brand{position:absolute;left:28px;top:44px;display:flex;align-items:center;gap:12px}
  .brand-dot{width:40px;height:40px;border-radius:50%;background:var(--accent)}
  .brand-name{font-size:34px;font-weight:400;color:var(--heading);letter-spacing:1px}
  .login{position:absolute;right:10px;top:14px;background:var(--nav);color:#fff;font-size:13px;padding:3px 8px}
  .main-nav{position:absolute;left:14px;top:118px;width:1084px;height:28px;background:var(--nav);display:flex}
  .main-nav a{color:#fff;text-decoration:none;font-size:17px;line-height:28px;padding:0 15px;border-right:2px solid var(--nav-line);text-transform:uppercase}
  .nav-accent{position:absolute;left:14px;top:150px;width:1084px;height:3px;background:var(--accent)}
  .hero{position:absolute;left:16px;top:160px;width:1080px;height:286px;overflow:hidden;
        background:linear-gradient(90deg,#3f5a4d 0%,#56725f 45%,#6a8170 70%,#c9a58b 88%,#e7ddd2 100%)}
  .hero-pager{position:absolute;left:6px;top:6px;display:flex;gap:4px}
  .hero-pager span{width:22px;height:22px;border:2px solid #fff;opacity:.8}
  .hero-pager span.is-active{background:#fff;opacity:1}
  .hero-caption{position:absolute;left:0;bottom:0;width:100%;height:66px;background:var(--caption-band);
        color:#fff;font-size:41px;line-height:66px;padding-left:28px;white-space:nowrap}
  .hero-caption strong{font-weight:700}
  .feature{position:absolute;top:470px;width:330px}
  .feature + .feature{border-left:1px solid var(--rule)}
  .feature-1{left:38px}
  .feature-2{left:362px;padding-left:42px;height:290px}
  .feature-3{left:728px;padding-left:38px;height:290px}
  .feature-label{font-size:15px;font-weight:700;color:var(--ink);margin-top:16px}
  .feature-title{font-size:29px;font-weight:400;color:var(--heading);margin-top:26px}
  .feature-text{font-size:16px;line-height:19px;color:var(--ink);margin-top:14px;width:290px}
  .learn-more{display:inline-flex;align-items:center;gap:10px;font-size:16px;font-weight:700;color:var(--heading);text-decoration:none;margin-top:20px}
  .copyright{position:absolute;left:54px;top:843px;font-size:11px;color:#555}
</style>
</head>
<body>
  <div class="page">
    <div class="brand"><span class="brand-dot"></span><span class="brand-name">47NOVA</span></div>
    <div class="login">Login</div>

    <nav class="main-nav">
      <a href="#">Company</a>
      <a href="#">Technical Services</a>
      <a href="#">Creative Services</a>
      <a href="#">Partners</a>
      <a href="#">Contact Us</a>
    </nav>
    <div class="nav-accent"></div>

    <section class="hero" role="img" aria-label="Photo of a student in glasses in front of a green chalkboard covered in trigonometry equations">
      <div class="hero-pager"><span class="is-active"></span><span></span><span></span><span></span><span></span><span></span></div>
      <div class="hero-caption"><strong>Smart:</strong> we don't believe in the word "overqualified"</div>
    </section>

    <article class="feature feature-1">
      <p class="feature-label">for graphic designers</p>
      <h2 class="feature-title">Get Creative!</h2>
      <p class="feature-text">47Nova is looking for top creative talent to deliver graphic design solutions for some leading global brands Do you have what it takes?</p>
      <a class="learn-more" href="#">Learn More <svg width="10" height="12" viewBox="0 0 10 12"><path d="M0 0L10 6L0 12Z" fill="var(--accent)"/></svg></a>
    </article>

    <article class="feature feature-2">
      <p class="feature-label">for clients</p>
      <h2 class="feature-title">The 47Nova Difference</h2>
      <p class="feature-text">Smart, Flexible, Thoughtful: find out why leading corporations and government agencies are turning to 47Nova to help manage their most demanding IT services challenges.</p>
      <a class="learn-more" href="#">Learn More <svg width="10" height="12" viewBox="0 0 10 12"><path d="M0 0L10 6L0 12Z" fill="var(--accent)"/></svg></a>
    </article>

    <article class="feature feature-3">
      <p class="feature-label">for partners</p>
      <h2 class="feature-title">Team Up With the Best</h2>
      <p class="feature-text">When it comes to technology partnerships, our mission it so make you a success.</p>
      <a class="learn-more" href="#">Learn More <svg width="10" height="12" viewBox="0 0 10 12"><path d="M0 0L10 6L0 12Z" fill="var(--accent)"/></svg></a>
    </article>
  </div>
  <p class="copyright">Copyright 2010, 47Nova, LLC All rights reserved.</p>
</body>
</html>
```